PAcifier/dummy design

Brand - Fable & Fern
Company - Australian designed ethical quality natural range.
Product - natural rubber soother/pacifier/dummy.
Box - 2 dummy's per box.
- hangable in store and stackable on shelf.
- box created with POS stand in mind would be amazing.
- box that is compact and easily ship-able.
- ideas - milk carton - or flat top milk carton style...
- matte finish.
Feel - modern, organic, boutique, clean and simplistic.
Natural product but for the boutique buyer, but can alos be placed in upmarket chemist, quality health food shop or chain store. target is not the hippy natural style, but the modern mama after something clean and quality.
for example - the mum from this page may buy it - https://www.instagram.com/pebbleandlark/
Colours & tones - matte finish.
- black logo
- white, cardboard tone, and soft tones included in the wreath in the images.
- current packaging image included.
Vision - designed in australia - made in Malaysia - exported to the world
Product variations
There are products that are the same but the brand sets them apart....
for example -
Breast feeding biscuits
A = cheap look https://www.instagram.com/mumcrumbsco/
B = quality look https://www.instagram.com/velmaspantry/
Lipgloss
A = cheap https://www.instagram.com/glintara_beauty/
B = quality https://www.instagram.com/dewbycorvell/
Boxes included - kanagroo - I had originally wanted an animal - i have decided to just get a beautiful packaging. simple, modern and lovely. I do like the font used in the kanagroo box tho
The other packaging designs are examples of what I thought - but the tall box will be hard to ship.
Target Market(s)
Baby - Organic natural modern mumma
Stores - premium pharmacies, baby boutiques. Department stores.

```html
<!DOCTYPE html>
<html lang="en">
<head>
<meta charset="utf-8">
<title>Fable &amp; Fern – Natural Rubber Pacifier Tag</title>
<link rel="stylesheet" href="https://fonts.googleapis.com/css2?family=Montserrat:wght@300;400;600;700&display=swap">
<style>
  :root {
    --kraft: #cdb594;
    --ink: #1e1e1e;
    --paper: #ffffff;
    --backdrop: #f4f4f4;
    --photo-light: #e4dccf;
    --photo-dark: #a8998a;
  }
  * { margin: 0; padding: 0; box-sizing: border-box; }
  html, body {
    width: 1200px;
    height: 1000px;
    overflow: hidden;
    background: var(--backdrop);
    font-family: "Montserrat", sans-serif;
  }
  .canvas {
    position: relative;
    width: 1200px;
    height: 1000px;
  }
  .hang-tag {
    position: absolute;
    left: 350px;
    top: 40px;
    width: 500px;
    height: 920px;
  }
  .tag-shape {
    position: absolute;
    inset: 0;
  }
  .age-badge {
    position: absolute;
    left: 26px;
    top: 42px;
    width: 88px;
    height: 88px;
    border: 2px solid var(--ink);
    border-radius: 50%;
    color: var(--ink);
    text-align: center;
    padding-top: 16px;
  }
  .age-badge .age-range {
    display: block;
    font-weight: 700;
    font-size: 26px;
    line-height: 1;
  }
  .age-badge .age-unit {
    display: block;
    font-weight: 300;
    font-size: 14px;
    margin-top: 2px;
  }
  .pack-badge {
    position: absolute;
    right: 28px;
    top: 62px;
    width: 72px;
    height: 72px;
    border: 2px solid var(--ink);
    border-radius: 14px;
    color: var(--ink);
    font-weight: 300;
    font-size: 17px;
    line-height: 1.15;
    text-align: center;
    padding-top: 13px;
  }
  .brand-name {
    position: absolute;
    left: 0;
    right: 0;
    top: 200px;
    text-align: center;
    color: var(--ink);
    font-weight: 400;
    font-size: 46px;
    letter-spacing: 1px;
  }
  .product-type {
    position: absolute;
    left: 0;
    right: 0;
    top: 326px;
    text-align: center;
    color: var(--ink);
  }
  .product-type .material {
    display: block;
    font-weight: 300;
    font-size: 25px;
    letter-spacing: 1px;
  }
  .product-type .category {
    display: block;
    font-weight: 700;
    font-size: 25px;
    letter-spacing: 11px;
    margin-left: 11px;
  }
  .product-photo {
    position: absolute;
    left: 75px;
    top: 408px;
    width: 350px;
    height: 350px;
    border-radius: 50%;
    background: radial-gradient(circle at 50% 45%, var(--photo-light), var(--photo-dark));
    outline: 3px solid var(--ink);
    outline-offset: 6px;
  }
  .product-name {
    position: absolute;
    left: 0;
    right: 0;
    top: 834px;
    text-align: center;
    color: var(--ink);
  }
  .product-name .title {
    display: block;
    font-weight: 600;
    font-size: 28px;
  }
  .product-name .subtitle {
    display: block;
    font-weight: 300;
    font-size: 19px;
    margin-top: 2px;
  }
</style>
</head>
<body>
<main class="canvas">
  <article class="hang-tag">
    <svg class="tag-shape" width="500" height="920" viewBox="0 0 500 920" aria-hidden="true">
      <rect x="0" y="0" width="500" height="920" rx="28" fill="var(--kraft)"/>
      <circle cx="250" cy="62" r="18" fill="var(--backdrop)"/>
      <path d="M0 300 H500 V800 C430 788 370 788 300 802 C230 816 160 822 90 810 C55 804 25 800 0 802 Z" fill="var(--paper)"/>
    </svg>

    <div class="age-badge">
      <span class="age-range">6|8</span>
      <span class="age-unit">months</span>
    </div>

    <div class="pack-badge">TWIN<br>PACK</div>

    <h1 class="brand-name">Fable &amp; Fern</h1>

    <h2 class="product-type">
      <span class="material">NATURAL RUBBER</span>
      <span class="category">PACIFIER</span>
    </h2>

    <div class="product-photo" role="img" aria-label="Soft-toned product photograph of the natural rubber pacifier"></div>

    <p class="product-name">
      <span class="title">Little Fern soother</span>
      <span class="subtitle">with an organic bamboo carry pouch</span>
    </p>
  </article>
</main>
</body>
</html>
```